A professional I.T consulting company requires a web design

Our company needs a fresh web design to help us drive our business forward. We are an Information Technology company who specialises in solutions based I.T delivery and consultations and who prides ourselves on our professional approach to business.

We would like a web site design from a designer who may be able to help us upload the site to WordPress and who may be interested in completing the "coding" section of the site (minimal coding). Although this is not essential to this project and won't factor into the decision making process.

A very thorough brief has been put together for this design project so very limited work is required in regards to content (the brief sets out all the content text - copy write material).

Please see the attached project documents for a copy of the brief

Target Market(s)

Please refer to the attached brief

Industry/Entity Type

Business

Requirements
Must have
• Please refer to the attached brief
Nice to have
Should not have

```html
<!DOCTYPE html>
<html lang="en">
<head>
<meta charset="utf-8">
<title>TARNIS – Information Technology Support</title>
<link href="https://fonts.googleapis.com/css2?family=Lato:ital,wght@0,300;0,400;0,700;1,300&display=swap" rel="stylesheet">
<style>
:root{
  --blue:#1e9ad6;
  --blue-dark:#1686bd;
  --ink:#4a4a4a;
  --muted:#7a7a7a;
  --white:#ffffff;
  --band:#a8a09b;
  --band-dark:#8f8782;
  --light:#ececec;
  --footer:#4b4b4b;
  --footer-line:#6a6a6a;
  --footer-text:#e4e4e4;
  --accent:#e8683a;
}
*{box-sizing:border-box;margin:0;padding:0}
html,body{width:760px;height:1200px;overflow:hidden}
body{position:relative;font-family:'Lato',sans-serif;color:var(--ink);background:var(--white)}
.abs{position:absolute}

/* header */
.site-header{left:0;top:0;width:760px;height:51px;background:var(--white)}
.brand{left:108px;top:12px;display:flex;align-items:center;gap:5px}
.brand-dot{width:26px;height:26px;border-radius:50%;background:var(--blue)}
.brand-name{font-weight:700;font-size:22px;color:var(--blue);letter-spacing:1px}
.header-contact{left:526px;top:10px;display:flex;align-items:flex-end;gap:4px}
.header-contact svg{margin-bottom:2px}
.contact-label{font-size:6px;color:var(--blue);font-weight:700;letter-spacing:.3px}
.contact-number{font-size:16px;color:#8a8a8a;font-weight:700;letter-spacing:-.3px;line-height:16px}

/* nav */
.main-nav{left:0;top:51px;width:760px;height:30px;background:linear-gradient(#27a6e0,var(--blue-dark))}
.nav-list{left:109px;top:0;height:30px;display:flex;align-items:center;list-style:none;gap:0}
.nav-list li{font-size:7.6px;color:var(--white);font-weight:700;letter-spacing:-.2px;margin-right:21px}
.nav-list li.current{font-size:8.4px}
.search{left:527px;top:57px;width:125px;height:19px;background:var(--white);border:1px solid #d6d6d6;display:flex}
.search span{flex:1;font-size:7.5px;color:#9a9a9a;padding:4px 4px}
.search i{width:21px;border-left:1px solid #d6d6d6;display:flex;align-items:center;justify-content:center}

/* hero */
.hero{left:0;top:81px;width:760px;height:298px;background:linear-gradient(100deg,#2d4a6a 0%,#5d7d9a 25%,#9bb6cf 45%,#d8e3ec 65%,#c9d8e6 100%)}
.hero-line{left:109px;height:25px;background:rgba(238,238,238,.92);color:var(--blue);font-size:12.6px;font-weight:300;padding:4px 10px;white-space:nowrap}
.hero-line.one{top:177px}
.hero-line.two{top:209px}
.hero-cta{left:109px;top:242px;height:23px;display:flex;background:var(--blue);color:var(--white);font-size:11px;font-weight:700}
.hero-cta span{padding:4px 9px}
.hero-cta b{width:23px;border-left:1px solid rgba(255,255,255,.35);display:flex;align-items:center;justify-content:center}
.dots{display:flex;gap:2px}
.dots i{width:7px;height:7px;border-radius:50%;background:var(--white);border:1px solid #bbb}
.dots i.on{background:var(--accent);border-color:var(--accent)}
.hero-dots{left:615px;top:367px}

/* welcome */
.welcome-title{left:109px;top:404px;font-size:19px;font-weight:400;color:#555;letter-spacing:-.6px}
.welcome-title em{font-style:normal;color:var(--blue)}
.welcome-text{left:109px;top:435px;width:540px;font-size:7.2px;line-height:12px;color:#666}

/* services */
.services{left:0;top:516px;width:760px;height:241px;background:linear-gradient(160deg,#b6aeaa,var(--band) 50%,var(--band-dark))}
.section-heading{left:109px;width:543px;display:flex;align-items:center;gap:12px}
.section-heading::before,.section-heading::after{content:"";flex:1;height:2px}
.services .section-heading{top:544px;color:var(--white)}
.services .section-heading::before,.services .section-heading::after{background:#8c8581}
.section-heading h2{font-size:16px;font-weight:400;letter-spacing:-.5px}
.services-text{left:109px;top:579px;width:543px;text-align:center;font-size:7.4px;line-height:11px;color:var(--white)}
.service{width:90px;text-align:center;top:640px}
.service svg{display:block;margin:0 auto}
.service p{font-size:12px;color:#2c2c2c;margin-top:2px;font-weight:400}

/* clients */
.clients{left:0;top:757px;width:760px;height:276px;background:var(--light)}
.clients .section-heading{top:786px;color:#666}
.clients .section-heading::before,.clients .section-heading::after{background:#c9c9c9}
.section-heading h2 em{font-style:normal;color:var(--blue)}
.client{width:100px;text-align:center;top:829px}
.client-photo{width:72px;height:72px;border-radius:50%;margin:0 auto;border:3px solid #f6f6f6;box-shadow:0 1px 3px rgba(0,0,0,.35);background:radial-gradient(circle at 50% 40%,#e9c6ad,#a87455 60%,#8b5a3e)}
.client p{font-size:8px;font-weight:700;color:#333;margin-top:12px}
.quote{left:140px;top:938px;width:490px;font-size:10.6px;line-height:18px;font-style:italic;font-weight:300;color:#9c9c9c}
.quote-mark{font-size:36px;color:#d2d2d2;font-family:'Lato',sans-serif;font-weight:700}
.client-dots{left:362px;top:1009px}

/* footer */
.site-footer{left:0;top:1033px;width:760px;height:167px;background:var(--footer)}
.footer-col{top:1057px;color:var(--footer-text)}
.footer-col h3{font-size:7.8px;font-weight:700;padding-bottom:5px;border-bottom:1px solid var(--footer-line);width:111px;margin-bottom:8px}
.footer-col ul{list-style:none}
.footer-col li{font-size:7px;line-height:13px;display:flex;align-items:center;gap:6px}
.footer-col li svg{flex:none}
.footer-brand{left:556px;top:1079px;display:flex;align-items:center;gap:4px}
.footer-brand .brand-dot{width:20px;height:20px;background:#d8d8d8}
.footer-brand .brand-name{font-size:17px;color:#d8d8d8}
.partner-badge{left:565px;top:1122px;width:87px;height:33px;background:linear-gradient(90deg,#e6e6e6,#c9c9c9)}
.footer-rule{left:109px;top:1172px;width:543px;height:1px;background:var(--footer-line)}
.copyright{left:110px;top:1182px;font-size:7px;color:var(--footer-text)}
</style>
</head>
<body>

<header class="abs site-header">
  <div class="abs brand"><span class="brand-dot"></span><span class="brand-name">TARNIS</span></div>
  <div class="abs header-contact">
    <svg width="14" height="18" viewBox="0 0 14 18"><path d="M3 1 L6 1 L7 5 L5 7 C6 10 7 12 9 13 L11 11 L14 13 L13 17 C6 17 1 10 1 3 Z" fill="#7d7d7d"/></svg>
    <div><div class="contact-label">CONATCT US</div><div class="contact-number">1300 - 555 - 010</div></div>
  </div>
</header>

<nav class="abs main-nav">
  <ul class="abs nav-list">
    <li class="current">HOME</li><li>ABOUT US</li><li>WHY TARNIS ?</li><li>SERVICES</li><li>SOLUTIONS</li><li>TECHNOLOGIES</li>
  </ul>
</nav>
<div class="abs search"><span>Search</span><i><svg width="10" height="10" viewBox="0 0 10 10"><circle cx="4" cy="4" r="3" fill="none" stroke="#777" stroke-width="1.2"/><line x1="6.2" y1="6.2" x2="9.5" y2="9.5" stroke="#777" stroke-width="1.4"/></svg></i></div>

<section class="abs hero" role="img" aria-label="Photo of two technicians checking a laptop beside a server rack full of network cables"></section>
<div class="abs hero-line one">TARNIS Provides Quality Information</div>
<div class="abs hero-line two">Technology Support And Solutions Services</div>
<div class="abs hero-cta"><span>Read More</span><b>»</b></div>
<div class="abs dots hero-dots"><i class="on"></i><i></i><i></i><i></i></div>

<h1 class="abs welcome-title">WELCOME TO <em>TARNIS</em></h1>
<p class="abs welcome-text">TARNIS is an Information Technology support and solution service provider founded and operating out of Westvale in regional Victoria. TARNIS was established in May of 2013 and since that time, has been providing technical advisory and managed service solutions throughout Westvale and the greater metropolitan areas.Our consultants are highly focused and committed to customer service and satisfaction and work hard to create lasting relationships with all we come into contact with. We pride ourselves on our personal investment into finding the right solution for our clients and in offering them a support network that is more akin to a personal relationship rather than a business partnership.</p>

<section class="abs services" role="img" aria-label="Faint background of business charts and graphs"></section>
<div class="abs section-heading" style="top:544px;color:#fff"><h2>OUR SERVICES</h2></div>
<p class="abs services-text">When it comes to your bussiness's&nbsp; I.T services needs,Tarnis provides you with Expertly delivered, unique I.T services, specifically designed to achieve your individual business goals and objectives.Our Consulting Services is an excellent way for our clients to access the expert skills and years of knowledge held with our I.T Engineers. This expertise is most commonly used for small, medium and large project works,</p>

<div class="abs service" style="left:111px">
  <svg width="74" height="74" viewBox="0 0 74 74"><polygon points="22,2 52,2 72,22 72,52 52,72 22,72 2,52 2,22" fill="#fff" stroke="#d8d8d8" stroke-width="2"/>
  <circle cx="37" cy="37" r="14" fill="none" stroke="#1e9ad6" stroke-width="7" stroke-dasharray="5 3.8"/><circle cx="37" cy="37" r="11" fill="#1e9ad6"/><circle cx="37" cy="37" r="5" fill="#fff"/></svg>
  <p>Services</p></div>
<div class="abs service" style="left:263px">
  <svg width="74" height="74" viewBox="0 0 74 74"><polygon points="22,2 52,2 72,22 72,52 52,72 22,72 2,52 2,22" fill="#fff" stroke="#d8d8d8" stroke-width="2"/>
  <path d="M37 18 C27 18 24 28 29 34 C32 38 32 40 32 43 L42 43 C42 40 42 38 45 34 C50 28 47 18 37 18 Z" fill="#1e9ad6"/><rect x="32" y="45" width="10" height="3" fill="#1e9ad6"/><rect x="33" y="50" width="8" height="3" rx="1" fill="#1e9ad6"/></svg>
  <p>Solutions</p></div>
<div class="abs service" style="left:409px">
  <svg width="74" height="74" viewBox="0 0 74 74"><polygon points="22,2 52,2 72,22 72,52 52,72 22,72 2,52 2,22" fill="#fff" stroke="#d8d8d8" stroke-width="2"/>
  <circle cx="37" cy="37" r="15" fill="none" stroke="#1e9ad6" stroke-width="6"/><circle cx="37" cy="37" r="8" fill="none" stroke="#1e9ad6" stroke-width="3"/><circle cx="37" cy="37" r="19" fill="none" stroke="#1e9ad6" stroke-width="1.5"/></svg>
  <p>Support</p></div>
<div class="abs service" style="left:560px">
  <svg width="74" height="74" viewBox="0 0 74 74"><polygon points="22,2 52,2 72,22 72,52 52,72 22,72 2,52 2,22" fill="#fff" stroke="#d8d8d8" stroke-width="2"/>
  <rect x="21" y="38" width="6" height="10" fill="#1e9ad6"/><rect x="29" y="33" width="6" height="15" fill="#1e9ad6"/><rect x="37" y="30" width="6" height="18" fill="#1e9ad6"/><rect x="45" y="26" width="6" height="22" fill="#1e9ad6"/></svg>
  <p>Technology</p></div>

<section class="abs clients"></section>
<div class="abs section-heading" style="top:786px;color:#666"><h2>OUR <em>CLIENTS</em></h2></div>

<div class="abs client" style="left:177px"><div class="client-photo" role="img" aria-label="Client portrait"></div><p>John Doe</p></div>
<div class="abs client" style="left:282px"><div class="client-photo" role="img" aria-label="Client portrait"></div><p>John Smith</p></div>
<div class="abs client" style="left:382px"><div class="client-photo" role="img" aria-label="Client portrait"></div><p>John&nbsp; Doe</p></div>
<div class="abs client" style="left:482px"><div class="client-photo" role="img" aria-label="Client portrait"></div><p>John&nbsp; Smith</p></div>

<span class="abs quote-mark" style="left:136px;top:922px">“</span>
<p class="abs quote">On the other hand, we denounce with righteous indignation and dislike men who are so beguiled and demoralized by the charms of pleasure of the moment, so blinded by desire, that they cannot foresee the pain and trouble that are bound to ensue; and equal blame belongs to those who fail in their duty through</p>
<span class="abs quote-mark" style="left:548px;top:966px">”</span>
<div class="abs dots client-dots"><i class="on"></i><i></i><i></i><i></i></div>

<footer class="abs site-footer"></footer>
<div class="abs footer-col" style="left:110px">
  <h3>LINKS</h3>
  <ul><li>Who We Are</li><li>What We Do</li><li>What We Offer</li><li>Our Mission</li><li>Our Vission</li></ul>
</div>
<div class="abs footer-col" style="left:260px">
  <h3>CONNECT US</h3>
  <ul>
    <li><svg width="7" height="7"><circle cx="3.5" cy="3.5" r="3" fill="#e4e4e4"/></svg>Friends Page</li>
    <li><svg width="7" height="7"><circle cx="3.5" cy="3.5" r="3" fill="#e4e4e4"/></svg>Short Posts</li>
    <li><svg width="7" height="7"><polygon points="1,0.5 6.5,3.5 1,6.5" fill="#e4e4e4"/></svg>Video Channel</li>
    <li><svg width="7" height="7"><circle cx="3.5" cy="3.5" r="3" fill="#e4e4e4"/></svg>Photo Boards</li>
  </ul>
</div>
<div class="abs footer-col" style="left:394px">
  <h3>CONTACT US</h3>
  <ul><li>P.O Box 410 Elmford Vic 3999</li><li>Ph:&nbsp; 1300&nbsp; 555&nbsp; 010</li><li>Fax: 00 25 4410 2207</li><li>E mail:</li><li>info@tarnis.example</li><li>www.tarnis.example</li></ul>
</div>
<div class="abs footer-brand"><span class="brand-dot"></span><span class="brand-name">TARNIS</span></div>
<div class="abs partner-badge"></div>
<div class="abs footer-rule"></div>
<p class="abs copyright">© 2014&nbsp; Tarnis. All Right&nbsp; Reserved.</p>

</body>
</html>
```